Valbrina Soletti Winery 2023 Label

We are just about to bottle our very first Napa Valley Cabernet Sauvignon and need label ideas

Target Market(s)

Cab drinkers who like Napa California Cabs

Industry/Entity Type

Wine Making

Logo Text

Valbrina Soletti 2023 Napa Estate Grown Cabernet Sauvignon

Requirements
Must have
• Winery Name, year of vintage and Napa Estate Cab
Nice to have
• If using the initials V and S use gold letters on black or red background

```html
<!DOCTYPE html>
<html lang="en">
<head>
<meta charset="utf-8">
<title>Valbrina Soletti 2023 Napa Estate Grown Cabernet Sauvignon</title>
<link rel="stylesheet" href="https://fonts.googleapis.com/css2?family=Tinos:wght@400&display=swap">
<style>
  :root {
    --label-black: #000000;
    --label-gold: #bd922f;
  }
  html, body {
    margin: 0;
    padding: 0;
    width: 1200px;
    height: 1200px;
    overflow: hidden;
    background: var(--label-black);
  }
  .wine-label {
    position: relative;
    width: 1200px;
    height: 1200px;
    background: var(--label-black);
    color: var(--label-gold);
    font-family: "Tinos", "Times New Roman", serif;
    font-weight: 400;
    overflow: hidden;
  }
  .label-line {
    position: absolute;
    left: 26px;
    width: 1200px;
    margin: 0;
    text-align: center;
    line-height: 1;
    white-space: nowrap;
    text-transform: uppercase;
  }
  .winery-name { font-size: 92px; }
  .winery-name--first { top: 225px; }
  .winery-name--second { top: 315px; }
  .initials {
    top: 448px;
    font-size: 170px;
    letter-spacing: -4px;
  }
  .vintage { top: 678px; font-size: 67px; }
  .region { top: 744px; font-size: 67px; }
  .estate { top: 817px; font-size: 82px; }
  .varietal { top: 905px; font-size: 64px; }
</style>
</head>
<body>
  <main class="wine-label">
    <h1 class="label-line winery-name winery-name--first">Valbrina</h1>
    <p class="label-line winery-name winery-name--second">Soletti</p>
    <p class="label-line initials" aria-label="Valbrina Soletti">VS</p>
    <p class="label-line vintage">2023</p>
    <p class="label-line region">Napa</p>
    <p class="label-line estate">Estate Grown</p>
    <p class="label-line varietal">Cabernet Sauvignon</p>
  </main>
</body>
</html>
```